We would like a business card that includes our logo on the front and the following information on the back:

Marcus Keene, Owner
Phone: (555) 614-8027
email: mkeenefencing@postvale.net

Marty Keene & Sons Fencing provides the following services:
Barbed wire
Smooth wire
High tensile
Electric

On the bottom of the card please add:
Please call or email Marcus for estimates.

```html
<!DOCTYPE html>
<html lang="en">
<head>
<meta charset="utf-8">
<title>Marty Keene &amp; Sons Fencing – Business Card</title>
<link rel="stylesheet" href="https://fonts.googleapis.com/css2?family=Cinzel:wght@600&family=Montserrat:wght@400;500&display=swap">
<style>
  :root {
    --stage: #c9c9c9;
    --card: #2b2321;
    --leather: #8a5a3b;
    --ink: #ffffff;
    --ink-soft: #ece7e4;
  }
  * { box-sizing: border-box; margin: 0; padding: 0; }
  html, body { width: 1200px; height: 788px; overflow: hidden; }
  body {
    background: var(--stage);
    font-family: "Montserrat", sans-serif;
    color: var(--ink);
    position: relative;
  }
  .card {
    position: absolute;
    top: 234px;
    width: 560px;
    height: 320px;
    background: var(--card);
    overflow: hidden;
    box-shadow: 0 8px 22px rgba(0,0,0,.25);
  }
  .card--back { left: 20px; }
  .card--front { left: 620px; }

  /* Brand wordmark */
  .wordmark {
    display: flex;
    align-items: center;
    gap: 10px;
    font-family: "Cinzel", serif;
    font-weight: 600;
    color: var(--ink);
    letter-spacing: .04em;
  }
  .wordmark__square { width: 10px; height: 10px; background: var(--ink); flex: none; }

  /* Back side */
  .back__brand {
    position: absolute; right: 34px; top: 34px;
    font-size: 15px;
  }
  .back__services {
    position: absolute; right: 34px; top: 78px;
    text-align: right;
    font-size: 11.5px;
    line-height: 1.45;
    color: var(--ink-soft);
  }
  .back__services ul { list-style: none; margin-top: 6px; font-size: 12px; }
  .back__services li::after {
    content: ""; display: inline-block; width: 4px; height: 4px;
    border-radius: 50%; background: var(--leather);
    margin-left: 5px; vertical-align: middle;
  }
  .contact {
    position: absolute; left: 34px; bottom: 42px;
  }
  .contact__name {
    font-family: "Cinzel", serif; font-weight: 600;
    color: var(--leather); font-size: 19px; letter-spacing: .03em;
  }
  .contact__role { font-size: 12px; color: var(--ink-soft); margin-bottom: 8px; }
  .contact__list { list-style: none; font-size: 12px; line-height: 1.7; color: var(--ink-soft); }
  .contact__list li { display: flex; align-items: center; gap: 8px; }
  .contact__list svg { width: 10px; height: 10px; fill: var(--leather); flex: none; }
  .contact__note { font-size: 12px; margin-top: 6px; color: var(--ink-soft); }
  .edge-band {
    position: absolute; left: 0; right: 0; bottom: 0; height: 14px;
    display: flex;
  }
  .edge-band__leather { width: 46%; background: var(--leather); }
  .edge-band__light { flex: 1; background: #f4f4f4; }

  /* Front side */
  .front__brand {
    position: absolute; inset: 0;
    justify-content: center;
    font-size: 24px;
  }
</style>
</head>
<body>

<section class="card card--back" aria-label="Card back">
  <div class="wordmark back__brand">
    <span class="wordmark__square"></span>Marty Keene &amp; Sons Fencing
  </div>

  <div class="back__services">
    <p>Marty Keene &amp; Sons Fencing<br>provides the following services:</p>
    <ul>
      <li>Barbed wire</li>
      <li>Smooth wire</li>
      <li>High tensile</li>
      <li>Electric</li>
    </ul>
  </div>

  <div class="contact">
    <p class="contact__name">MARCUS KEENE</p>
    <p class="contact__role">Owner</p>
    <ul class="contact__list">
      <li><svg viewBox="0 0 10 10" aria-hidden="true"><path d="M2 0.5l2 2-1 1.2c.6 1.3 1.5 2.2 2.8 2.8L7 5.5l2 2-1.2 1.8C4.5 9 1 5.5.5 2.2z"/></svg>(555) 614-8027</li>
      <li><svg viewBox="0 0 10 10" aria-hidden="true"><path d="M0 2h10v6H0zM.6 2.4L5 5.6l4.4-3.2v.9L5 6.5.6 3.3z"/></svg>mkeenefencing@postvale.net</li>
      <li><svg viewBox="0 0 10 10" aria-hidden="true"><circle cx="5" cy="5" r="5"/></svg>www.mkeenefencing.net</li>
    </ul>
    <p class="contact__note">Please call or email Marcus for estimates.</p>
  </div>

  <div class="edge-band"><span class="edge-band__leather"></span><span class="edge-band__light"></span></div>
</section>

<section class="card card--front" aria-label="Card front">
  <div class="wordmark front__brand">
    <span class="wordmark__square"></span>Marty Keene &amp; Sons Fencing
  </div>
</section>

</body>
</html>
```